Business Cards Needed For Veterinary Business

Looking for a business card design for a veterinary blood bank. We would like it to be clean and professional on appearance but still warm and inviting. We would like to utilize our logo and similar coloring. We will use our phone number, email, website, employee name, employee title.

We do not want a bunch of animated animal photos but do not need the style to be as clinical as a laboratory or human medical procedure office.

We are looking for some creative ideas to choose from so that we can generate a standout professional business card for our management team to utilize.

Target Market(s)

professionals

Industry/Entity Type

veterinary

Contact Information for Business Card

employee name, employee title, phone number, website URL, email

Font styles to use
Sans Serif

Colors
0054AA
0677BA
7BADD7
CADEEF
E8F1F8
EB3D1F
EC4F4E
F09395
F8D3D4
FCEDEE

Requirements
Nice to have
• creative design
Should not have
• animated photos

```html
<!DOCTYPE html>
<html lang="en">
<head>
<meta charset="utf-8">
<title>Harbor Veterinary Blood Bank – Business Card</title>
<link href="https://fonts.googleapis.com/css2?family=Montserrat:wght@400;500;600;700;800&display=swap" rel="stylesheet">
<style>
  :root{
    --brand-blue:#0054AA;
    --brand-blue-mid:#0677BA;
    --brand-red:#EB3D1F;
    --brand-red-soft:#EC4F4E;
    --ink-grey:#55585c;
    --card-white:#ffffff;
    --stage:#1c1c1e;
  }
  *{margin:0;padding:0;box-sizing:border-box}
  html,body{width:1200px;height:900px;overflow:hidden}
  body{background:var(--stage);font-family:"Montserrat",sans-serif;position:relative}

  .card{position:absolute;width:700px;height:400px;border-radius:22px;overflow:hidden}

  /* Front */
  .card-front{left:110px;top:40px;background:var(--brand-blue)}
  .front-lockup{position:absolute;left:0;right:0;top:0;bottom:0;display:flex;align-items:center;justify-content:center;gap:26px}
  .front-dot{width:86px;height:86px;border-radius:50%;background:var(--brand-red);flex:none}
  .front-name{color:#fff;font-weight:700;font-size:34px;line-height:1.15;letter-spacing:.5px;text-transform:uppercase}

  /* Back */
  .card-back{left:390px;top:470px;background:var(--card-white)}
  .back-wordmark{position:absolute;left:48px;top:46px;color:var(--brand-red);font-weight:800;font-size:24px;line-height:1.15;text-transform:uppercase;letter-spacing:.3px}
  .back-mark{position:absolute;right:50px;top:70px;width:240px;height:240px;border-radius:50%;background:var(--brand-red)}

  .person{position:absolute;left:48px;top:162px;padding-left:20px}
  .person-bar{position:absolute;left:0;top:0;width:24px;height:54px;background:var(--brand-blue);left:-48px;width:40px}
  .person-name{font-weight:800;font-size:26px;letter-spacing:.5px;text-transform:uppercase}
  .person-name .first{color:var(--brand-blue)}
  .person-name .last{color:var(--brand-red)}
  .person-title{color:var(--ink-grey);font-size:15px;font-weight:500;margin-top:2px;letter-spacing:.4px}

  .address{position:absolute;left:68px;top:238px;color:var(--ink-grey);font-size:14px;line-height:1.5;letter-spacing:.4px}

  .contacts{position:absolute;left:68px;top:292px;list-style:none;color:var(--ink-grey);font-size:14px;letter-spacing:.4px}
  .contacts li{display:flex;align-items:center;gap:10px;height:26px}
  .contacts svg{width:14px;height:14px;fill:var(--brand-red);flex:none}
</style>
</head>
<body>

<section class="card card-front" aria-label="Card front">
  <div class="front-lockup">
    <span class="front-dot"></span>
    <div class="front-name">Harbor Veterinary<br>Blood Bank</div>
  </div>
</section>

<section class="card card-back" aria-label="Card back">
  <div class="back-wordmark">Harbor Veterinary<br>Blood Bank</div>

  <div class="person">
    <span class="person-bar"></span>
    <div class="person-name"><span class="first">Daniel</span> <span class="last">Whitcombe</span></div>
    <div class="person-title">Owner &amp; Manager</div>
  </div>

  <div class="address">P.O. Box Linden Street<br>Country Name AB, T4B 2K9</div>

  <ul class="contacts">
    <li>
      <svg viewBox="0 0 24 24"><path d="M6.6 10.8a15.1 15.1 0 0 0 6.6 6.6l2.2-2.2c.3-.3.7-.4 1-.2 1.1.4 2.3.6 3.6.6.6 0 1 .4 1 1V20c0 .6-.4 1-1 1A17 17 0 0 1 3 4c0-.6.4-1 1-1h3.5c.6 0 1 .4 1 1 0 1.3.2 2.5.6 3.6.1.3 0 .7-.2 1z"/></svg>
      15550123456
    </li>
    <li>
      <svg viewBox="0 0 24 24"><path d="M3 5h18c.6 0 1 .4 1 1v12c0 .6-.4 1-1 1H3c-.6 0-1-.4-1-1V6c0-.6.4-1 1-1zm9 7.2L4.5 7v1.9L12 14l7.5-5.1V7z"/></svg>
      info@harborvetbloodbank.com
    </li>
    <li>
      <svg viewBox="0 0 24 24"><path d="M12 2a10 10 0 1 0 0 20 10 10 0 0 0 0-20zm6.9 6h-3a15.7 15.7 0 0 0-1.3-3.6A8 8 0 0 1 18.9 8zM12 4c.8 1.2 1.5 2.5 1.9 4h-3.8c.4-1.5 1.1-2.8 1.9-4zM4.3 14a8.2 8.2 0 0 1 0-4h3.4a16.5 16.5 0 0 0 0 4zm.8 2h3a15.7 15.7 0 0 0 1.3 3.6A8 8 0 0 1 5.1 16zm3-8h-3a8 8 0 0 1 4.3-3.6C8.8 5.5 8.4 6.7 8.1 8zM12 20c-.8-1.2-1.5-2.5-1.9-4h3.8c-.4 1.5-1.1 2.8-1.9 4zm2.3-6H9.7a14.7 14.7 0 0 1 0-4h4.6a14.7 14.7 0 0 1 0 4zm.3 5.6c.6-1.1 1-2.3 1.3-3.6h3a8 8 0 0 1-4.3 3.6zM16.3 14a16.5 16.5 0 0 0 0-4h3.4a8.2 8.2 0 0 1 0 4z"/></svg>
      www.harborvetbloodbank.com
    </li>
  </ul>

  <span class="back-mark"></span>
</section>

</body>
</html>
```